The Ledgerline Business Card

Business card with QR Code for an accounting and tax business

Target Market(s)

Small Business and Individual Tax

Industry/Entity Type

Bookkeeping, Accounting and Taxes

Contact Information for Business Card

482 CALDWELL ST STE 2210 #614273 BOSTON, MA Zip: 02387

Requirements
Must have
• Name and Address

```html
<!DOCTYPE html>
<html lang="en">
<head>
<meta charset="utf-8">
<title>The Ledgerline Business Card</title>
<link href="https://fonts.googleapis.com/css2?family=Playfair+Display:wght@600&family=Arimo:wght@400&display=swap" rel="stylesheet">
<style>
  :root {
    --page: #2a2a2a;
    --card-front: #ffffff;
    --card-back: #262626;
    --card-back-deep: #1c1c1c;
    --ink: #1f1f1f;
    --ink-soft: #3a3a3a;
    --faint: #ececec;
    --light: #ffffff;
  }
  * { box-sizing: border-box; margin: 0; padding: 0; }
  html, body { width: 1200px; height: 900px; overflow: hidden; }
  body {
    background: var(--page);
    display: flex;
    flex-direction: column;
    align-items: center;
    justify-content: center;
    gap: 40px;
  }
  .card {
    position: relative;
    width: 700px;
    height: 400px;
    border-radius: 28px;
    overflow: hidden;
  }
  .card-front { background: var(--card-front); color: var(--ink); }

  .brand {
    position: absolute;
    left: 150px;
    top: 52px;
    display: flex;
    flex-direction: column;
    align-items: center;
    gap: 12px;
  }
  .brand-dot {
    width: 62px; height: 62px;
    border: 7px solid var(--ink);
    border-radius: 50%;
  }
  .brand-name {
    font-family: "Playfair Display", serif;
    font-weight: 600;
    font-size: 34px;
    letter-spacing: 1px;
    color: var(--ink);
    padding-bottom: 6px;
    border-bottom: 1.5px solid var(--ink);
  }

  .address {
    position: absolute;
    left: 60px;
    top: 196px;
    font-family: "Arimo", sans-serif;
    font-size: 17px;
    line-height: 23px;
    color: var(--ink-soft);
  }
  .contacts {
    position: absolute;
    left: 60px;
    top: 258px;
    list-style: none;
    font-family: "Arimo", sans-serif;
    font-size: 17px;
    line-height: 27px;
    color: var(--ink-soft);
  }
  .contacts li { display: flex; align-items: center; gap: 8px; }
  .contacts svg { width: 13px; height: 13px; fill: var(--ink); flex: none; }

  .person {
    position: absolute;
    right: 56px;
    top: 178px;
    text-align: right;
  }
  .person-name {
    font-family: "Playfair Display", serif;
    font-weight: 600;
    font-size: 26px;
    letter-spacing: 0.5px;
    color: var(--ink);
  }
  .person-role {
    font-family: "Arimo", sans-serif;
    font-size: 17px;
    color: var(--ink-soft);
    margin-top: 2px;
  }

  .front-ring {
    position: absolute;
    left: 430px;
    top: 250px;
    width: 250px;
    height: 250px;
    border: 22px solid var(--faint);
    border-radius: 50%;
  }

  .card-back { background: var(--card-back); }
  .back-pattern {
    position: absolute;
    inset: 0;
    background: linear-gradient(135deg, var(--card-back) 0%, var(--card-back-deep) 100%);
  }
  .back-mark {
    position: absolute;
    right: 48px;
    bottom: 44px;
    display: flex;
    align-items: center;
    gap: 10px;
  }
  .back-dot {
    width: 30px; height: 30px;
    border: 4px solid var(--light);
    border-radius: 50%;
  }
  .back-name {
    font-family: "Playfair Display", serif;
    font-weight: 600;
    font-size: 20px;
    color: var(--light);
  }
</style>
</head>
<body>
  <section class="card card-front">
    <div class="front-ring"></div>

    <div class="brand">
      <div class="brand-dot"></div>
      <div class="brand-name">The Ledgerline</div>
    </div>

    <p class="address">482 CALDWELL ST STE 2210 #614273<br>Boston, Ma Zip: 02387</p>

    <ul class="contacts">
      <li>
        <svg viewBox="0 0 16 16"><path d="M3.6 1.2l2.3 2.6-1.4 2a9 9 0 0 0 5.7 5.7l2-1.4 2.6 2.3-1.6 2.3C6.9 16.2-.2 9.1.9 2.8z"/></svg>
        555.014.2290
      </li>
      <li>
        <svg viewBox="0 0 16 16"><path d="M1 3h14v1.2L8 9 1 4.2z M1 5.8l7 4.8 7-4.8V13H1z"/></svg>
        info@theledgerline.com
      </li>
      <li>
        <svg viewBox="0 0 16 16"><path d="M8 1a7 7 0 1 0 0 14A7 7 0 0 0 8 1zm0 1.5c.9 0 1.9 1.6 2.2 4H5.8C6.1 4.1 7.1 2.5 8 2.5zM2.6 7.5h1.7c0-.3.1 1.5.3 1H2.6zm0 1h2.2c.1 2 .6 3.5 1.3 4.3A5.5 5.5 0 0 1 2.6 8.5zm3.2 0h4.4c-.3 2.4-1.3 4-2.2 4s-1.9-1.6-2.2-4zm5.4 0h2.2a5.5 5.5 0 0 1-3.5 4.3c.7-.8 1.2-2.3 1.3-4.3zm0-1c-.1-2-.6-3.5-1.3-4.3a5.5 5.5 0 0 1 3.5 4.3zm-6.4 0H2.6a5.5 5.5 0 0 1 3.5-4.3c-.7.8-1.2 2.3-1.3 4.3z"/></svg>
        www.theledgerline.com
      </li>
    </ul>

    <div class="person">
      <div class="person-name">DORIAN WELLES</div>
      <div class="person-role">CEO/Founder</div>
    </div>
  </section>

  <section class="card card-back">
    <div class="back-pattern" role="img" aria-label="Repeating tone-on-tone pattern of the brand mark across a dark card"></div>
    <div class="back-mark">
      <div class="back-dot"></div>
      <div class="back-name">The Ledgerline</div>
    </div>
  </section>
</body>
</html>
```